Redesign of business card for Birchline Mechanical

We are looking for a new design for our business cards for Birchline Mechanical. We are a plumbing & HVAC construction company, operating on the West Coast of Canada and USA. Logo attached.
Industry/Entity Type
Construction - Plumbing & HVAC
Contact Information for Business Card
Name, address, phone numbers, email, website address
Look and feel
Each slider illustrates characteristics of the customer's brand and the style your logo design should communicate.

```html
<!DOCTYPE html>
<html lang="en">
<head>
<meta charset="utf-8">
<title>Birchline Mechanical – Business Card</title>
<link rel="stylesheet" href="https://fonts.googleapis.com/css2?family=Montserrat:wght@400;700&display=swap">
<style>
  :root {
    --ink: #1f1f1f;
    --band: #2a2a2a;
    --paper: #ffffff;
    --text-light: #f2f2f2;
    --text-muted: #d8d8d8;
    --stage: #e9e6e2;
    --pattern-dark: #0c0c0c;
    --pattern-mid: #262626;
  }
  * { margin: 0; padding: 0; box-sizing: border-box; }
  html, body {
    width: 1200px; height: 900px; overflow: hidden;
    background: var(--stage);
    font-family: "Montserrat", Arial, sans-serif;
  }
  .canvas {
    position: relative; width: 1200px; height: 900px;
  }
  .card {
    position: absolute; left: 250px; width: 700px; height: 400px;
    border-radius: 26px; overflow: hidden;
    box-shadow: 0 10px 24px rgba(0,0,0,.25);
  }
  /* Back */
  .card-back { top: 40px; background: var(--pattern-dark); }
  .back-pattern {
    position: absolute; inset: 0;
    background: linear-gradient(135deg, var(--pattern-mid) 0%, var(--pattern-dark) 60%, #111 100%);
  }
  .back-brand {
    position: absolute; right: 48px; bottom: 60px;
    display: flex; align-items: center; gap: 10px;
    color: var(--paper); font-weight: 700; font-size: 15px; letter-spacing: 1px;
    text-transform: uppercase;
  }
  .brand-square {
    width: 16px; height: 16px; background: currentColor;
  }
  /* Front */
  .card-front { top: 460px; background: var(--band); }
  .front-top {
    position: absolute; left: 0; top: 0; width: 100%; height: 178px;
    background: var(--paper);
    display: flex; align-items: center; justify-content: center; gap: 16px;
    color: var(--ink);
  }
  .front-top .brand-square { width: 34px; height: 34px; }
  .front-brand {
    font-weight: 700; font-size: 34px; letter-spacing: 2px; text-transform: uppercase;
  }
  .contact-block {
    position: absolute; left: 0; top: 178px; width: 100%; height: 222px;
    color: var(--text-light);
  }
  .person {
    position: absolute; right: 390px; top: 42px; text-align: right;
  }
  .person-name { font-weight: 700; font-size: 27px; }
  .person-role { font-size: 16px; color: var(--text-muted); margin-top: 2px; letter-spacing: .5px; }
  .divider {
    position: absolute; left: 332px; top: 38px; width: 2px; height: 100px; background: var(--text-light);
  }
  .contact-list {
    position: absolute; left: 356px; top: 40px; list-style: none;
    font-size: 17px; letter-spacing: .3px;
  }
  .contact-list li { display: flex; align-items: center; gap: 12px; height: 32px; }
  .contact-list svg { width: 16px; height: 16px; fill: var(--text-light); flex: none; }
  .address {
    position: absolute; left: 0; width: 100%; top: 160px; text-align: center;
    font-size: 17px; letter-spacing: .3px;
  }
</style>
</head>
<body>
<main class="canvas">
  <section class="card card-back" aria-label="Card back">
    <div class="back-pattern" role="img" aria-label="Repeating gloss-black brand monogram pattern"></div>
    <div class="back-brand"><span class="brand-square"></span>Birchline Mechanical</div>
  </section>

  <section class="card card-front" aria-label="Card front">
    <header class="front-top">
      <span class="brand-square"></span>
      <span class="front-brand">Birchline Mechanical</span>
    </header>
    <div class="contact-block">
      <div class="person">
        <p class="person-name">Daniel Harlow</p>
        <p class="person-role">Managing Director</p>
      </div>
      <span class="divider"></span>
      <ul class="contact-list">
        <li>
          <svg viewBox="0 0 24 24" aria-hidden="true"><path d="M6.6 10.8a15.1 15.1 0 0 0 6.6 6.6l2.2-2.2a1 1 0 0 1 1-.25 11.4 11.4 0 0 0 3.6.57 1 1 0 0 1 1 1V20a1 1 0 0 1-1 1A17 17 0 0 1 3 4a1 1 0 0 1 1-1h3.5a1 1 0 0 1 1 1c0 1.25.2 2.45.57 3.57a1 1 0 0 1-.25 1z"/></svg>
          555.014.2290
        </li>
        <li>
          <svg viewBox="0 0 24 24" aria-hidden="true"><path d="M2 5h20v2l-10 6L2 7z M2 9l10 6 10-6v10H2z"/></svg>
          info@birchlinemechanical.com
        </li>
        <li>
          <svg viewBox="0 0 24 24" aria-hidden="true"><path d="M12 2a10 10 0 1 0 0 20 10 10 0 0 0 0-20zm6.9 6h-3a15 15 0 0 0-1.3-4A8 8 0 0 1 18.9 8zM12 4c.8 1.2 1.5 2.6 1.9 4h-3.8c.4-1.4 1.1-2.8 1.9-4zM4.3 14a8 8 0 0 1 0-4h3.4a16 16 0 0 0 0 4zm.8 2h3a15 15 0 0 0 1.3 4A8 8 0 0 1 5.1 16zm3-8h-3a8 8 0 0 1 4.3-4 15 15 0 0 0-1.3 4zM12 20c-.8-1.2-1.5-2.6-1.9-4h3.8c-.4 1.4-1.1 2.8-1.9 4zm2.3-6H9.7a14 14 0 0 1 0-4h4.6a14 14 0 0 1 0 4zm.3 6a15 15 0 0 0 1.3-4h3a8 8 0 0 1-4.3 4zm1.7-6a16 16 0 0 0 0-4h3.4a8 8 0 0 1 0 4z"/></svg>
          www.birchlinemechanical.com
        </li>
      </ul>
      <p class="address">218 Harbor Ridge Lane Salem, OR 97301</p>
    </div>
  </section>
</main>
</body>
</html>
```